Business Card Design

We need business cards designed incorporating our graphics/logo already used on our trucks. We are a small construction company that does everything from building new homes, additions, Kitchens, Baths, Decks, Hardwood Floors/Tile, all phases of construction. No job is too small. We pride ourselves on True Craftmanship/Customer Satisfaction, its what truly separates us from everyone else.

Industry/Entity Type

Construction

Contact Information for Business Card

Maple Ridge Renovations Lic#27KP51986400
342 51st Avenue Gull Harbor NJ 08901
(555)731-2948 Email: info@mapleridgeexample.com
Paul Vandermolen

```html
<!DOCTYPE html>
<html lang="en">
<head>
<meta charset="utf-8">
<title>Maple Ridge Renovations – Business Card</title>
<link rel="stylesheet" href="https://fonts.googleapis.com/css2?family=Noto+Sans:wght@400;500&family=Questrial&display=swap">
<style>
  :root {
    --paper: #ffffff;
    --ink: #111111;
    --night: #000000;
    --stripe-light: #eef0f7;
    --stripe-dark: #9a9cb5;
    --badge: #9ed3ee;
    --reverse: #ffffff;
  }
  * { margin: 0; padding: 0; box-sizing: border-box; }
  html, body {
    width: 1200px; height: 702px; overflow: hidden;
    background: var(--paper);
  }
  .card {
    position: relative; width: 1200px; height: 702px;
    background: var(--paper);
    font-family: "Noto Sans", "Segoe UI", sans-serif;
    color: var(--ink);
  }
  .brand-mark {
    position: absolute; left: 60px; top: 97px;
    width: 260px; height: 192px;
    display: flex; align-items: center; gap: 14px;
  }
  .brand-mark__square {
    flex: none; width: 44px; height: 44px; background: var(--badge);
  }
  .brand-mark__name {
    font-size: 26px; font-weight: 500; line-height: 1.15; color: var(--ink);
  }
  .company {
    position: absolute; right: 64px; top: 148px; text-align: right;
  }
  .company__name { font-size: 41px; font-weight: 500; line-height: 1.15; }
  .company__licence { font-size: 31px; font-weight: 500; line-height: 1.15; }
  .band-rule {
    position: absolute; left: 0; top: 332px; width: 1200px; height: 18px;
    background: var(--night);
  }
  .band-texture {
    position: absolute; left: 0; top: 350px; width: 1200px; height: 61px;
    background: linear-gradient(180deg, var(--stripe-light), var(--stripe-dark) 50%, var(--stripe-light));
  }
  .footer {
    position: absolute; left: 0; top: 411px; width: 1200px; height: 291px;
    background: var(--night); color: var(--reverse);
  }
  .contact-person {
    position: absolute; right: 854px; top: 88px; text-align: right;
    font-size: 31px; line-height: 40px;
  }
  .contact-office {
    position: absolute; right: 64px; top: 88px; text-align: right;
    font-size: 31px; line-height: 40px;
  }
  .contact-office__address {
    font-family: "Questrial", "Century Gothic", sans-serif;
    font-size: 30px;
    letter-spacing: 1.6px;
  }
</style>
</head>
<body>
  <div class="card">
    <div class="brand-mark">
      <span class="brand-mark__square"></span>
      <span class="brand-mark__name">Maple Ridge Renovations</span>
    </div>

    <div class="company">
      <div class="company__name">Maple Ridge Renovations</div>
      <div class="company__licence">Lic#27KP51986400</div>
    </div>

    <div class="band-rule"></div>
    <div class="band-texture" role="img" aria-label="Fine diagonal line texture band"></div>

    <div class="footer">
      <div class="contact-person">
        <div class="contact-person__name">Paul Vandermolen</div>
        <div class="contact-person__phone">(555)731-2948</div>
      </div>
      <div class="contact-office">
        <div class="contact-office__email">Email: info@mapleridgeexample.com</div>
        <div class="contact-office__address">342 51st Avenue Gull Harbor NJ 08901</div>
      </div>
    </div>
  </div>
</body>
</html>
```